Pelican Crest landing page design

We need a landing page designed for an ecommerce website that sales fresh US domestic shrimp from the Gulf of Mexico and ships them direct to the consumer "From Our Shore To Your Door". For the landing page, we would like customers to be able to place an order and or inquire further about our product as well as links to social media. The company logo is attached

1 page

```html
<!DOCTYPE html>
<html lang="en">
<head>
<meta charset="utf-8">
<title>Pelican Crest — Fresh Domestic Shrimp</title>
<link href="https://fonts.googleapis.com/css2?family=Merienda:wght@400;700&family=Montserrat:wght@400;600;700&display=swap" rel="stylesheet">
<style>
  :root {
    --page-bg: #fbdfd0;
    --brand-orange: #f46511;
    --ink: #4a4a4a;
    --white: #ffffff;
    --hero-dark: #1b1d21;
    --hero-warm: #3a2c26;
  }
  * { box-sizing: border-box; margin: 0; padding: 0; }
  html, body {
    width: 1200px;
    height: 594px;
    overflow: hidden;
    background: var(--page-bg);
    font-family: "Montserrat", Arial, sans-serif;
  }
  .page { position: relative; width: 1200px; height: 594px; }

  .site-header {
    position: absolute;
    top: 11px; left: 160px; right: 160px;
    height: 46px;
    display: flex;
    align-items: center;
    justify-content: space-between;
  }
  .brand { display: flex; align-items: center; gap: 8px; text-decoration: none; }
  .brand-mark {
    width: 44px; height: 44px;
    border: 1px solid #a9a9a9;
    border-radius: 50%;
  }
  .brand-name {
    font-size: 17px;
    font-weight: 600;
    letter-spacing: 2px;
    color: var(--ink);
    text-transform: uppercase;
  }
  .social-links { display: flex; gap: 6px; list-style: none; }
  .social-links a {
    display: block;
    width: 24px; height: 24px;
    border-radius: 50%;
    background: var(--brand-orange);
  }

  .promo-bar {
    position: absolute;
    top: 62px; left: 120px;
    width: 960px; height: 44px;
    background: var(--brand-orange);
    box-shadow: 0 2px 4px rgba(0,0,0,0.2);
    display: flex; align-items: center; justify-content: center;
    color: var(--white);
    font-size: 10.5px;
    text-transform: uppercase;
  }

  .hero {
    position: absolute;
    top: 127px; left: 120px;
    width: 960px; height: 400px;
    overflow: hidden;
    box-shadow: 0 2px 5px rgba(0,0,0,0.3);
  }
  .hero-photo {
    position: absolute; inset: 0;
    background: linear-gradient(160deg, var(--hero-warm) 0%, var(--hero-dark) 70%);
  }
  .hero-content {
    position: absolute; inset: 0;
    text-align: center;
    color: var(--white);
  }
  .hero-title {
    position: absolute;
    top: 80px; left: 0; right: 0;
    font-family: "Merienda", cursive;
    font-size: 31px;
    line-height: 36px;
    font-weight: 400;
    letter-spacing: 1px;
    text-transform: uppercase;
  }
  .hero-title .accent { color: var(--brand-orange); }
  .hero-subtitle {
    position: absolute;
    top: 120px; left: 0; right: 0;
    font-size: 11.5px;
    font-weight: 700;
    text-transform: uppercase;
  }
  .shop-now {
    position: absolute;
    top: 188px; left: 445px;
    width: 70px;
    padding-bottom: 4px;
    border-bottom: 2px solid var(--white);
    color: var(--white);
    font-size: 10.5px;
    font-weight: 700;
    text-decoration: none;
    text-transform: uppercase;
  }
  .explore-more {
    position: absolute;
    top: 300px; left: 0; right: 0;
    font-size: 8.5px;
    text-transform: uppercase;
  }
  .explore-dots {
    position: absolute;
    top: 320px; left: 478px;
  }

  .site-footer {
    position: absolute;
    top: 556px; right: 160px;
    font-size: 8px;
    color: var(--ink);
  }
</style>
</head>
<body>
<div class="page">
  <header class="site-header">
    <a class="brand" href="#">
      <span class="brand-mark"></span>
      <span class="brand-name">Pelican Crest</span>
    </a>
    <ul class="social-links">
      <li><a href="#" aria-label="Social profile 1"></a></li>
      <li><a href="#" aria-label="Social profile 2"></a></li>
      <li><a href="#" aria-label="Social profile 3"></a></li>
      <li><a href="#" aria-label="Social profile 4"></a></li>
      <li><a href="#" aria-label="Social profile 5"></a></li>
    </ul>
  </header>

  <div class="promo-bar">Shipping from our shore to your door</div>

  <section class="hero">
    <div class="hero-photo" role="img" aria-label="Photograph of cooked Gulf shrimp on dark slate with lemon wedges and fresh mint"></div>
    <div class="hero-content">
      <h1 class="hero-title">Fresh Domestic <span class="accent">Shrimp</span></h1>
      <p class="hero-subtitle">From the Gulf of Mexico</p>
      <a class="shop-now" href="#">Shop Now</a>
      <p class="explore-more">Explore More</p>
      <svg class="explore-dots" width="4" height="14" viewBox="0 0 4 14" aria-hidden="true">
        <circle cx="2" cy="2" r="1.6" fill="#fff"/>
        <circle cx="2" cy="7" r="1.6" fill="#fff"/>
        <circle cx="2" cy="12" r="1.6" fill="#fff"/>
      </svg>
    </div>
  </section>

  <footer class="site-footer">Copyright © &nbsp;2019</footer>
</div>
</body>
</html>
```